Business Card, A4 Letter Head and DL Envelope for Brandolux

We are looking for a design for our Business Card, A4 Letter Head and DL Envelope.

Brandolux is a distributor of promotional products. We specialize in a range of branded promotional products, these include pens, polo shirts, key rings, drink bottles, uniforms and bags to name a few. We are experts in marketing and assist companies in choosing the right promotional product for their needs. We will predominately be an online business where customers visit our website and browse our range of promotional products and branding options.

Our colours are black, red, white and grey.

Files must be supplied in eps, pdf and ai format.

Please display the following information:
Dorian Pell
Account Manager
Suite xxx, 214 Harwick Lane Melbourne, Victoria 3000
Phone +61 3 5550 1842
Mobile +61 455 501 736
sales@brandolux.example
www.brandolux.example

```html
<!DOCTYPE html>
<html lang="en">
<head>
<meta charset="utf-8">
<title>Brandolux – DL Envelope</title>
<link rel="stylesheet" href="https://fonts.googleapis.com/css2?family=Arimo:wght@400;700&display=swap">
<style>
  :root {
    --paper: #ffffff;
    --charcoal: #2b2b2b;
    --brand-red: #d21f26;
    --band-grey: #9d9d9d;
    --ink: #1f1f1f;
    --wordmark: #4a4a4a;
  }
  * { margin: 0; padding: 0; box-sizing: border-box; }
  html, body {
    width: 1200px;
    height: 550px;
    overflow: hidden;
    background: var(--paper);
  }
  .envelope {
    position: relative;
    width: 1200px;
    height: 550px;
    background: var(--paper);
    font-family: "Arimo", Arial, sans-serif;
    overflow: hidden;
  }
  .envelope__shapes {
    position: absolute;
    inset: 0;
    width: 1200px;
    height: 550px;
  }
  .corner-band { fill: var(--charcoal); }
  .corner-stripe { fill: none; stroke: var(--brand-red); stroke-width: 4; }
  .footer-band { fill: var(--band-grey); }

  .brand {
    position: absolute;
    left: 87px;
    top: 38px;
    display: flex;
    align-items: center;
    gap: 14px;
  }
  .brand__dot {
    width: 66px;
    height: 66px;
    border-radius: 50%;
    background: var(--brand-red);
  }
  .brand__name {
    font-size: 27px;
    font-weight: 700;
    color: var(--wordmark);
    letter-spacing: 0.5px;
    text-transform: uppercase;
  }

  .contact {
    position: absolute;
    left: 66px;
    right: 52px;
    top: 470px;
    color: var(--ink);
  }
  .contact__address {
    font-size: 25px;
    letter-spacing: 4.2px;
    white-space: nowrap;
  }
  .contact__lines {
    margin-top: 8px;
    display: flex;
    justify-content: space-between;
    font-size: 22px;
    letter-spacing: 0.6px;
    white-space: nowrap;
  }
</style>
</head>
<body>
  <main class="envelope">
    <svg class="envelope__shapes" viewBox="0 0 1200 550" aria-hidden="true">
      <path class="corner-band" d="M0,0 H452 C330,36 170,66 0,92 Z"/>
      <path class="corner-stripe" d="M452,0 C330,38 170,68 0,94"/>
      <path class="footer-band" d="M0,462 C420,456 860,440 1200,388 V550 H0 Z"/>
    </svg>

    <header class="brand">
      <span class="brand__dot"></span>
      <span class="brand__name">Brandolux</span>
    </header>

    <footer class="contact">
      <p class="contact__address">Suite xxx, 214 Harwick Lane Melbourne, Victoria 3000</p>
      <p class="contact__lines">
        <span class="contact__phone">T: +61 3 5550 1842</span>
        <span class="contact__email">E: sales@brandolux.example</span>
        <span class="contact__web">www.brandolux.example</span>
      </p>
    </footer>
  </main>
</body>
</html>
```